Ledger Ready Business Card

I need a business card designed around my logo (which was designed here on Sketch Yard!)

Target Market(s)

Professional Businesses

Industry/Entity Type

Business

Requirements
Must have
• Details that must be on the business card:

Harriet Vantos
Director
0491 263 358
harriet@ledgerready.com.au
www.ledgerready.com.au
PO Box 4471 Fitzroy North Vic 3068

```html
<!DOCTYPE html>
<html lang="en">
<head>
<meta charset="utf-8">
<title>Ledger Ready Business Card</title>
<link rel="stylesheet" href="https://fonts.googleapis.com/css2?family=Tinos:wght@700&display=swap">
<style>
  :root {
    --page: #ece8e3;
    --orange: #f26522;
    --cocoa: #5a4a43;
    --tan: #c69c6d;
    --brand-red: #c8202a;
    --ink-dark: #3a2e2a;
    --white: #ffffff;
  }
  * { margin: 0; padding: 0; box-sizing: border-box; }
  html, body { width: 1200px; height: 1200px; overflow: hidden; }
  body {
    background: var(--page);
    font-family: "Tinos", "Times New Roman", serif;
    font-weight: 700;
    position: relative;
  }
  .card {
    position: absolute;
    left: 170px;
    width: 860px;
    height: 500px;
    border: 12px solid var(--orange);
    border-radius: 34px;
    overflow: hidden;
  }
  .card--front { top: 70px; background: var(--cocoa); }
  .card--back  { top: 630px; background: var(--tan); }

  .front-brand {
    position: absolute;
    inset: 0;
    display: flex;
    align-items: center;
    justify-content: center;
    gap: 26px;
  }
  .front-brand__square {
    width: 70px; height: 70px;
    background: var(--brand-red);
  }
  .front-brand__name {
    color: var(--white);
    font-size: 64px;
    letter-spacing: 1px;
  }

  .band {
    position: absolute;
    background: var(--orange);
    transform-origin: left center;
  }
  .band--top {
    left: 0; right: 0; top: 40px;
    height: 10px;
  }
  .band--top-thin {
    left: 0; right: 0; top: 22px;
    height: 4px;
  }
  .band--lower {
    left: -40px; top: 160px;
    width: 1000px; height: 18px;
    transform: rotate(17deg);
  }
  .band--lower-thin {
    left: -40px; top: 230px;
    width: 1000px; height: 6px;
    transform: rotate(17deg);
  }

  .back-brand {
    position: absolute;
    left: 80px; top: 75px;
    display: flex;
    align-items: center;
    gap: 18px;
    z-index: 1;
  }
  .back-brand__square {
    width: 44px; height: 44px;
    background: var(--brand-red);
  }
  .back-brand__name {
    color: var(--ink-dark);
    font-size: 50px;
    letter-spacing: 1px;
  }

  .contact {
    position: absolute;
    left: 300px; top: 168px;
    color: var(--white);
    z-index: 1;
  }
  .contact__name { font-size: 44px; line-height: 1; padding-left: 20px; }
  .contact__role {
    display: inline-block;
    font-size: 40px;
    line-height: 1;
    margin-top: 4px;
    padding: 0 12px 6px 60px;
    border-bottom: 2px solid var(--white);
  }
  .contact__lines { margin-top: 16px; padding-left: 60px; }
  .contact__line { font-size: 28px; line-height: 1.36; }
  .contact__line--small { font-size: 23px; }
</style>
</head>
<body>
  <section class="card card--front" aria-label="Card front">
    <div class="front-brand">
      <span class="front-brand__square"></span>
      <span class="front-brand__name">Ledger Ready</span>
    </div>
  </section>

  <section class="card card--back" aria-label="Card back">
    <div class="band band--top-thin" aria-hidden="true"></div>
    <div class="band band--top" aria-hidden="true"></div>
    <div class="band band--lower" aria-hidden="true"></div>
    <div class="band band--lower-thin" aria-hidden="true"></div>

    <div class="back-brand">
      <span class="back-brand__square"></span>
      <span class="back-brand__name">Ledger Ready</span>
    </div>

    <div class="contact">
      <p class="contact__name">Harriet Vantos</p>
      <p class="contact__role">Director</p>
      <div class="contact__lines">
        <p class="contact__line">Tell: 0491 263 358</p>
        <p class="contact__line">Email:harriet@ledgerready.com.au</p>
        <p class="contact__line">www.ledgerready.com.au</p>
        <p class="contact__line contact__line--small">PO Box 4471 Fitzroy North Vic 3068</p>
      </div>
    </div>
  </section>
</body>
</html>
```